Greek Souvlaki Restaurant Menu Design

We would like to redesign our menu (at the moment just a price-list without any graphics) and create something more fun.

You can find all the items we are offering at the following link / our e-shop:
https://olivebranchkitchen.example/orders/en/order/
I have also attached a printout of the above with hand written notes on the sections and items that will be included.

Our menu is divided to a couple of parts:
- Souvlaki Bar and Grill
- Authentic Greek Cuisine
- Wine List
- Desserts
- Bakaliko

This project will take on the first part of our menu, which is the Souvlaki Bar and Grill. If we are happy with your design, we will then develop the rest of our menu.

Souvlaki Bar and Grill
---------------------------

Our souvlaki can be customised to the customer requirements. The following links have similar set ups:

WOW!Patty
https://gr.pinboardly.example/pin/100000000000000001/
I like the way they have set it up, but the graphics and colours used are not my thing. I also like they way they have split up the steps, choose, top it of, etc.

The Krokk
https://gr.pinboardly.example/pin/100000000000000002/
I hate the step 1,2,3 on the left side. It does not make it playful. Like the fact that they have used pictures of the ingredients.

https://gr.pinboardly.example/pin/100000000000000003/
Hate the graphics, like the concept.

-------------

First Sections: Our Souvliaki Pita Wrap

The steps to customise a souvlaki can be found on the following link:
https://olivebranchkitchen.example/orders/en/order/ and choose pita wrap.

Most of the one side of our Souvliaki/Grill menu should be dedicated to our Pita Wraps.

It should have a small description of the Greek Souvlaki Pita Wrap. Something along the lines of "Get a whole meal all wrapped up with our delicious Greek Pita Wraps. Containing protein, sauce and salad". Improvements of this line are welcome.

It should then have the steps to customise it.

Step One.
Choose Base:
1. Chicken Skewer
2. Pork Skewer
3. etc
Price and options can be found on the above link on our website

Step Two.
Add one of our delicious home made sauces.
Options can be found on our website.

Step Three
Finalise it with the ingredients of your choice.
The customer can select multiple incredients

Step Four.
Feeling Hungry? Add extras:
Extras and Prices can be found on the link provided.

Buy two wraps and save. Takeaway only!
You will find this option as "Double Souvlaki Pita Wrap Offer."
Instead of 2x5.5 = £11 pay £10.5. This offer should also be mentioned somewhere on this section.

-----

Second Section - Our Platters

Skewers Platter and Gyros Platter

Options can be found by clicking on the items on the link provided.

Extras and Pita Bread option are common. Meat options are different and skewers have a choice of side. Meat options have 2/3 skewers and 200/300 grams of gyros, so they can probably be combined somehow.

These section can also be called Naked / Open Souvlaki Platters

Third Section
From Our Grill

All options from this section together with modifiers (can be see if you click on each item). I would like pictures from each item.

Forth Section
Meal Deals, starter combo and Set Menu.

Meal Deal for 1/2 and 4 are wraps with extras. The for 4 is not on the pdf and will be up on our website soon, so please check. I think those are easy to e incorporated next to the pita wrap section as upgrades to save.

Set menus are various items.

If they can fit on this page somehow we incorporate them, if not we can make a separate page with the offers / meals deals. If a separate page is created them the meal deal from our kitchen and vegetarean set menu should also be included.

Fifth Section
Salads and Starter

I would like all options from Hot and Cold starter and our salad. I would like pictures next to all options, if possible.

-----

Final notes/ideas.

Wraps, platters and grill could be one page front and back. Salads and starters could be a different page(s) or sections.

The menu should be easily updated and we would like a format where we can update prices and descriptions.

Prices and descriptions can be found on the link provided.

Feel free to improve our descriptions and titles. Please do mention where you made improvements, so we can approve them.

Our kitchen, dessert and wine menu will be given as a separate project and priority will be given to the person that won this competition.

If you need better quality pictures please let us know, most of the pictures we do have them in raw format too.

------

Some designs that I like. To give you an idea of the design I would like to see:

https://www.craftmarketly.example/listing/100000001/american-menu-restaurant-cafe-menus
I would love to see something like that for the grill/salad/starter side of our menu, since it has space for pictures.

https://gr.pinboardly.example/pin/100000000000000004/
I would love to see something like that, where the incredients of a souvlaki come together. This is optional and does not have to be there.

https://gr.pinboardly.example/pin/100000000000000005/

https://gr.pinboardly.example/pin/100000000000000006/

https://gr.pinboardly.example/pin/100000000000000007/

https://gr.pinboardly.example/pin/100000000000000008/

Target Market(s)

London

Font styles to use
Serif
Sans Serif

Colors
abd037
3277b5
33a6d7

Requirements
Must have
• Build your own souvlaki section. See description for examples.

Pictures for starters and salads.

Should be elegant
Nice to have
• Incorporate our relevant meal deals on the souvlaki pita section

```html
<!DOCTYPE html>
<html lang="en">
<head>
<meta charset="utf-8">
<title>Souvlaki Pita Wrap &amp; Platters Menu</title>
<link href="https://fonts.googleapis.com/css2?family=Caveat+Brush&family=Share+Tech+Mono&family=Nunito:wght@400;700;800&display=swap" rel="stylesheet">
<style>
:root{
  --paper:#dcdbd8;
  --paper-dark:#cfcecb;
  --wood:#2a2a2a;
  --ink:#2f2f2f;
  --ink-soft:#555;
  --white:#ffffff;
  --veg:#8cc63f;
  --dots:#9a9a9a;
}
*{margin:0;padding:0;box-sizing:border-box}
html,body{width:777px;height:1200px;overflow:hidden;background:var(--wood)}
.menu{position:relative;width:777px;height:1200px;overflow:hidden;
  background:radial-gradient(ellipse at 40% 30%,#e3e2df 0%,var(--paper) 55%,var(--paper-dark) 100%);
  color:var(--ink);font-family:"Nunito",sans-serif}
.wood-left{position:absolute;left:0;top:0;width:28px;height:1200px;background:linear-gradient(90deg,#1e1e1e,#353535)}
.wood-bottom{position:absolute;left:0;bottom:0;width:777px;height:32px;background:linear-gradient(#353535,#1e1e1e)}
.edge-dots{position:absolute;left:755px;top:0;height:1200px;border-left:2px dotted #bbb}

/* header */
.banner{position:absolute;left:0;top:24px;width:746px;height:80px;background:var(--white);
  clip-path:polygon(0 4%,100% 0,97% 50%,100% 100%,0 96%)}
.banner::before,.banner::after{content:"";position:absolute;left:6px;right:30px;border-top:2px dotted var(--dots)}
.banner::before{top:5px}.banner::after{bottom:5px}
.headline{position:absolute;left:16px;top:24px;width:330px;white-space:nowrap;font-family:"Caveat Brush",cursive;font-size:46px;font-weight:400;line-height:80px;color:var(--ink)}
.tagline{position:absolute;left:358px;top:36px;width:370px;white-space:nowrap;font-family:"Caveat Brush",cursive;font-size:20px;line-height:26px;color:var(--ink)}

/* step boxes */
.label-box{position:absolute;border:1.5px solid #444;font-family:"Share Tech Mono",monospace;font-size:17px;line-height:21px;padding-left:6px;letter-spacing:1px;color:var(--ink);white-space:nowrap}
.list{position:absolute;list-style:none;font-size:10.6px;line-height:14px;color:var(--ink);white-space:nowrap}
.list b{font-weight:800}
.veg{display:inline-block;width:9px;height:9px;border-radius:50%;background:var(--veg);vertical-align:-1px;margin-left:2px}
.side-note{position:absolute;font-family:"Caveat Brush",cursive;font-size:15px;color:var(--ink-soft);transform:rotate(-90deg);transform-origin:left top;white-space:nowrap}

.title{position:absolute;font-family:"Share Tech Mono",monospace;font-weight:400;color:var(--ink);letter-spacing:1px;white-space:nowrap}
.desc{position:absolute;font-size:10.4px;line-height:13.6px;color:var(--ink-soft)}

.photo{position:absolute}
.divider{position:absolute;border-top:2px dotted var(--dots)}

/* offer */
.offer{position:absolute;left:264px;top:538px;width:336px;height:64px;background:var(--white);
  clip-path:polygon(0 0,100% 0,100% 100%,0 100%,8% 50%)}
.offer-kicker{position:absolute;left:302px;top:545px;font-family:"Share Tech Mono",monospace;font-size:14px;letter-spacing:.5px;white-space:nowrap}
.offer-kicker em{font-family:"Caveat Brush",cursive;font-style:normal;font-size:14px;margin-left:6px}
.offer-name{position:absolute;left:302px;top:564px;font-weight:800;font-size:14px;letter-spacing:-.2px;white-space:nowrap}
.offer-note{position:absolute;left:302px;top:582px;font-weight:700;font-size:11px;white-space:nowrap}
.offer-photo{position:absolute;left:590px;top:516px;width:144px;height:144px;border-radius:50%;border:4px dotted #999;background:var(--white);padding:6px}
.offer-photo div{width:100%;height:100%;border-radius:50%;background:radial-gradient(circle at 50% 45%,#c49a62,#9b7a55 55%,#cfd3d8 80%)}

.brand{position:absolute;left:540px;top:1060px;width:110px;text-align:center;font-family:"Share Tech Mono",monospace;font-size:22px;line-height:24px;color:var(--ink)}
</style>
</head>
<body>
<main class="menu">
  <div class="wood-left"></div>
  <div class="wood-bottom"></div>
  <div class="edge-dots"></div>

  <header>
    <div class="banner"></div>
    <h1 class="headline">Make it Your Own!</h1>
    <p class="tagline">A FULL MEAL wrapped in our<br>delicious Greek pita, customized by you...</p>
  </header>

  <section class="steps">
    <div class="label-box" style="left:62px;top:126px;width:214px;height:24px">1 THE MAIN THING</div>
    <span class="side-note" style="left:64px;top:216px">Choose 1</span>
    <ul class="list" style="left:88px;top:153px">
      <li><b>Chicken</b> £ .50</li>
      <li><b>Pork</b> £ .50</li>
      <li><b>Gyros Chicken</b> £ 1.50</li>
      <li><b>Gyros Pork</b> £ 1.50</li>
      <li><b>Mixed Gyros</b> (Chicken &amp; Pork) £ 2.00</li>
      <li><b>Kebab</b> (Lamb &amp; Beef) £ .50</li>
      <li><b>Sausage</b> £ .50</li>
      <li><b>Haloumi</b> <span class="veg"></span> £ .50</li>
      <li><b>No Base</b> <span class="veg"></span></li>
    </ul>

    <div class="label-box" style="left:62px;top:292px;width:214px;height:24px">2 MAKE IT SAUCY</div>
    <span class="side-note" style="left:64px;top:380px">Choose 1</span>
    <ul class="list" style="left:88px;top:320px">
      <li><b>Tzatziki</b> <span class="veg"></span></li>
      <li><b>Tyrokafteri</b> <span class="veg"></span></li>
      <li><b>Burger Sauce</b></li>
      <li><b>No Sauce</b></li>
    </ul>

    <div class="label-box" style="left:62px;top:389px;width:214px;height:24px">3 FILL'ER UP</div>
    <span class="side-note" style="left:66px;top:452px">Any</span>
    <ul class="list" style="left:88px;top:416px">
      <li><b>Fries</b></li>
      <li><b>Tomatoes</b></li>
      <li><b>Onions</b></li>
    </ul>

    <div class="label-box" style="left:62px;top:470px;width:214px;height:24px">4 FEED YOUR HUNGER!</div>
    <span class="side-note" style="left:64px;top:582px">Add extras:</span>
    <ul class="list" style="left:88px;top:497px">
      <li><b>Double Pita Bread</b> £ 1.00</li>
      <li><b>add Pork Skewer</b> £ 2.50</li>
      <li><b>add Chicken Skewer</b> £ 2.50</li>
      <li><b>add Kebab</b> (lamb+beef) £ 2.50</li>
      <li><b>add Sausage</b> £ 2.50</li>
      <li><b>add Haloumi</b> £ 1.90</li>
    </ul>
  </section>

  <section class="wrap-intro">
    <h2 class="title" style="left:302px;top:122px;font-size:31px">SOUVLAKI PITA WRAP</h2>
    <p class="desc" style="left:302px;top:161px;width:372px">Get a whole meal all wrapped up with our Greek pita wraps. Choose the base (meat skewers, gyros, haloumi or kebab) you want. Then add one of our delicious home made sauces. Finalise it with the ingredients of your choice. If you are feeling extra hungry you can double up your pita or add extra base. It will leave you craving them time and time again! &nbsp;£ 5.50</p>
    <div class="photo" role="img" aria-label="Olive sprig decoration" style="left:680px;top:134px;width:46px;height:106px;border-radius:40px;background:linear-gradient(#c8c7c4,#bdbcb9);opacity:.6"></div>
    <div class="photo" role="img" aria-label="Photo of a souvlaki pita wrap with fries, tomato and tzatziki in a paper wrapper" style="left:316px;top:250px;width:396px;height:286px;border-radius:40% 30% 35% 45%;background:radial-gradient(ellipse at 55% 45%,#d7a25c 0%,#b98a58 40%,#a68766 60%,#eef0f3 78%,rgba(238,240,243,0) 90%)"></div>
  </section>

  <aside>
    <div class="offer"></div>
    <p class="offer-kicker">BUY TWO WRAPS AND SAVE!<em>Takeaway only!</em></p>
    <p class="offer-name">DOUBLE SOUVLAKI PITA WRAP OFFER</p>
    <p class="offer-note">You know the steps......two for £10.5</p>
    <div class="offer-photo" role="img" aria-label="Photo of two souvlaki pita wraps"><div></div></div>
  </aside>

  <div class="divider" style="left:160px;top:632px;width:288px"></div>

  <section class="platters">
    <h2 class="title" style="left:68px;top:644px;font-size:31px">NAKED SOUVLAKI PLATTERS</h2>

    <h3 class="title" style="left:66px;top:694px;font-size:18px">GYROS PLATTER</h3>
    <p class="desc" style="left:66px;top:716px;width:340px">Traditional Greek Juicy Pork or Chicken Gyros. Generous portion served with refreshing tzatziki sauce, pita bread, fries, onion, tomatoes and lettuce. A great selection of ingredients make it a delicious complete meal! &nbsp;£ 13.00</p>

    <div class="label-box" style="left:56px;top:778px;width:220px;height:24px;font-size:15px">MEAT OPTIONS 200G</div>
    <ul class="list" style="left:65px;top:806px">
      <li><b>Chicken Gyros</b> 200g</li>
      <li><b>Pork Gyros</b> 200g</li>
      <li><b>Mixed Gyros</b> (Chicken &amp; Pork) 200g + £ 1.00</li>
      <li><span style="font-family:'Share Tech Mono',monospace;font-size:12px">UPGRADE TO 300G</span> + £ 3.50</li>
      <li><b>Mixed</b> + £ 4.00</li>
    </ul>

    <div class="label-box" style="left:306px;top:778px;width:128px;height:24px;font-size:15px">EXTRAS</div>
    <ul class="list" style="left:316px;top:806px">
      <li><b>Extra Haloumi</b> + £ 3.50</li>
      <li><b>Extra Tzatziki</b> + £ 3.00</li>
    </ul>
    <div class="label-box" style="left:306px;top:838px;width:128px;height:24px;font-size:15px">PITA BREAD</div>
    <ul class="list" style="left:316px;top:865px">
      <li><b>No Pita</b></li>
      <li><b>1 x Pita</b></li>
      <li><b>2 x Pita</b>+ £ 1.00</li>
    </ul>

    <div class="photo" role="img" aria-label="Photo of a gyros platter with fries, onion, tomato and tzatziki" style="left:468px;top:692px;width:248px;height:180px;border-radius:50%;background:radial-gradient(ellipse at 45% 45%,#8a6140 0%,#b57c45 35%,#d8584a 55%,#f7f7f5 72%)"></div>

    <div class="divider" style="left:64px;top:926px;width:608px"></div>

    <h3 class="title" style="left:66px;top:936px;font-size:18px">SKEWERS PLATTER</h3>
    <p class="desc" style="left:66px;top:958px;width:350px">Our delicious skewers or kebab. Homemade souvlaki is taken from the best part of the meat to create the perfect succulent grilled experience. Served with fries or salad and pitta bread. &nbsp;£ 10.00</p>

    <div class="label-box" style="left:56px;top:1006px;width:222px;height:24px;font-size:15px">MEAT OPTIONS 2 SKEWERS</div>
    <ul class="list" style="left:66px;top:1033px">
      <li><b>2 x Chicken Skewers</b></li>
      <li><b>2 x Pork Skewers</b></li>
      <li><b>2 x Kebab</b> (Lamb &amp; Beef)</li>
    </ul>
    <div class="label-box" style="left:58px;top:1083px;width:130px;height:24px;font-size:15px">SIDES</div>
    <ul class="list" style="left:66px;top:1109px">
      <li><b>Fries</b></li>
      <li><b>Side Salad</b> + £ 2.50</li>
    </ul>

    <div class="label-box" style="left:306px;top:1006px;width:132px;height:24px;font-size:15px">EXTRAS</div>
    <ul class="list" style="left:316px;top:1033px">
      <li><b>Extra Haloumi</b> + £ 3.50</li>
      <li><b>Extra Tzatziki</b> + £ 3.00</li>
      <li><b>Extra Skewer</b> + £ 3.50</li>
    </ul>
    <div class="label-box" style="left:306px;top:1082px;width:132px;height:24px;font-size:15px">PITA BREAD</div>
    <ul class="list" style="left:316px;top:1110px">
      <li><b>No Pita</b></li>
      <li><b>1 x Pita</b></li>
      <li><b>2 x Pita</b> + £ 1.00</li>
    </ul>

    <div class="photo" role="img" aria-label="Photo of grilled chicken skewers on fries and pita" style="left:460px;top:948px;width:276px;height:78px;border-radius:10px;background:linear-gradient(90deg,#f0c04a 0%,#c98a4e 35%,#b9763f 65%,#e9e7e2 100%)"></div>
  </section>

  <div class="brand">OLIVE<br>BRANCH<br>KITCHEN</div>
</main>
</body>
</html>
```